Bright Quest Appeal needs a brochure

I need an A4 - Two sided brochure design.
It's for a maths challenge fundraiser for primary schools throughout Australia.
It needs to be bright and fun with the pictures / files supplied,
Please use as many pics as you can, more the better...
Also keep Logos as transparent
See our website for an idea of what we do pls. thebrightquest.example
Pls make it FUN ....NOT corporate..
so curves and colours rather than straight lines
The only headings that need to be ALL capitals is "FREE TO JOIN" & "FUNDRAISER" Other titles not all capitals pls
Please note: when putting in the pics of the games, pls put in order from game1-7 as they go in order of the school grade levels (Preschool to Grade 6). showing teachers how they become more difficult...in that order.
This brochure will be sent to schools.
Schools have admin open letters, we get about 2 - 3 seconds for admin to decide to keep or bin the brochure, so they need to see it's a fundraiser and "free to join" in those seconds.
cheers
- fun style maybe marker felt or comic sans but you choose any other you think works to make it fun

```html
<!DOCTYPE html>
<html lang="en">
<head>
<meta charset="utf-8">
<title>Bright Quest Appeal – Maths Challenge Brochure</title>
<link href="https://fonts.googleapis.com/css2?family=Gluten:wght@700;800&family=Sniglet:wght@400;800&family=Mali:wght@500;600&display=swap" rel="stylesheet">
<style>
  :root{
    --bg:#a9f3e4;
    --teal:#1ed3a0;
    --teal-deep:#13b88a;
    --red:#e5263a;
    --pink:#d6246e;
    --navy:#1d2a8f;
    --orange:#f2a21c;
    --paper:#f6f7f7;
  }
  *{box-sizing:border-box;margin:0;padding:0}
  html,body{width:1200px;height:1200px;overflow:hidden}
  body{background:var(--bg);position:relative;font-family:"Mali",cursive}
  .page{position:absolute;top:204px;width:560px;height:792px;background:var(--paper);overflow:hidden;box-shadow:0 10px 24px rgba(0,80,70,.18)}
  .page--front{left:27px}
  .page--back{left:613px}
  .photo-wash{position:absolute;left:0;top:40px;width:560px;height:300px;
    background:linear-gradient(180deg,rgba(241,215,200,.55),rgba(217,232,239,.35) 55%,rgba(246,247,247,0));}
  .band{position:absolute;left:0;width:560px}
  .band--top{top:0;height:120px}
  .band--bottom{bottom:0;height:90px}
  .brand{position:absolute;left:18px;top:16px;display:flex;align-items:center;gap:6px;
    font-family:"Sniglet",cursive;font-weight:800;font-size:15px;color:var(--navy)}
  .brand__dot{width:22px;height:22px;border-radius:50%;background:var(--red)}
  .block{position:absolute;left:40px;right:40px;text-align:center}
  .tagline{font-family:"Sniglet",cursive;font-size:13px;color:var(--navy)}
  .kicker{font-family:"Sniglet",cursive;font-size:22px;color:var(--orange)}
  .headline{font-family:"Gluten",cursive;font-weight:800;color:var(--teal);letter-spacing:1px;line-height:1}
  .headline--xl{font-size:62px}
  .headline--lg{font-size:52px}
  .subhead{font-family:"Sniglet",cursive;font-weight:400;font-size:18px;color:var(--navy)}
  .body{font-size:11px;line-height:1.25;color:var(--red)}
  .free{font-family:"Sniglet",cursive;font-size:25px;color:var(--teal);letter-spacing:1px}
  .effortless{font-family:"Gluten",cursive;font-weight:700;font-size:23px;color:var(--navy);letter-spacing:1px}
  .certificate{position:absolute;left:17px;top:480px;width:84px;height:120px;border-radius:2px;
    background:linear-gradient(135deg,#e9b844,#c88a1e)}
  .steps{position:absolute;left:100px;right:70px;top:262px;list-style:none}
  .steps li{position:relative;text-align:center;font-size:11px;line-height:1.45;color:var(--red);margin-bottom:2px}
  .steps li::before{content:"";position:absolute;left:-18px;top:6px;width:4px;height:4px;border-radius:50%;background:var(--red)}
  .games-title{font-family:"Sniglet",cursive;font-size:13px;color:var(--navy)}
  .games{position:absolute;left:42px;right:30px;display:flex;justify-content:center;gap:8px}
  .game{width:114px;height:66px;border-radius:2px}
  .game--1{background:linear-gradient(135deg,#3b2a8f,#a21e6a)}
  .game--2{background:linear-gradient(135deg,#3e6fd8,#c9612e)}
  .game--3{background:linear-gradient(135deg,#2fa83a,#1b6e1d)}
  .game--4{background:linear-gradient(135deg,#101a3e,#2b6fd0)}
  .game--5{background:linear-gradient(135deg,#1d4fc2,#0e2b78)}
  .game--6{background:linear-gradient(135deg,#0d1d5c,#2a3c8e)}
  .game--7{background:linear-gradient(135deg,#14182b,#3c4866)}
  .contact{position:absolute;left:20px;font-family:"Sniglet",cursive;font-size:12px;color:var(--navy);line-height:1.55}
  .contact a{color:var(--teal-deep);text-decoration:none}
  .contact .phone{color:var(--teal-deep);font-size:10.5px}
  .contact .brand-inline{display:flex;align-items:center;gap:6px;margin:4px 0 6px;font-weight:800}
</style>
</head>
<body>

<section class="page page--front">
  <div class="photo-wash" role="img" aria-label="Faded photo of smiling primary school students"></div>
  <svg class="band band--top" viewBox="0 0 560 120" preserveAspectRatio="none">
    <path d="M0 0H560V30C470 22 400 40 360 80C330 110 240 112 0 82Z" fill="var(--teal)"/>
    <path d="M0 82C240 112 330 110 360 80C400 40 470 22 560 30V38C470 30 410 50 370 86C335 118 240 120 0 90Z" fill="var(--red)"/>
    <path d="M0 90C240 120 335 118 370 86C410 50 470 30 560 38V44C470 36 418 56 378 90C340 122 240 124 0 96Z" fill="var(--pink)" opacity=".6"/>
  </svg>
  <div class="brand"><span class="brand__dot"></span>Bright Quest Appeal</div>

  <p class="block tagline" style="top:145px">Fun games developing confidence in mathematics.</p>
  <p class="block kicker" style="top:166px">Maths Challenge</p>
  <h1 class="block headline headline--xl" style="top:196px">FUNDRAISER</h1>
  <p class="block body" style="top:262px;font-size:9.5px">"A great fundraiser helping primary school students with maths!"</p>

  <h2 class="block subhead" style="top:306px">Students love a challenge!</h2>
  <p class="block body" style="top:330px;left:120px;right:120px">Students are challenged to solve educational maths games on The Bright Quest website.</p>

  <h2 class="block subhead" style="top:381px;left:10px;right:10px">It's lots of fun and helps students with maths!</h2>
  <p class="block body" style="top:405px;left:110px;right:110px">A maths challenge designed to build confidence in mathematics for Australian Primary School students.</p>
  <p class="block body" style="top:446px;left:110px;right:110px">Once students have completed their maths challenge, they may download a certificate of congratulations.</p>

  <div class="certificate" role="img" aria-label="Gold certificate of congratulations"></div>
  <p class="block free" style="top:484px">FREE TO JOIN!</p>
  <p class="block effortless" style="top:516px">Effortless to run!</p>
  <p class="block body" style="top:553px;left:110px;right:110px">It's all set-up online and ready to go. No spending time or effort planning activities or fundraiser days.</p>
  <p class="block body" style="top:596px;left:100px;right:100px">The Bright Quest website is fully safe and secure with no information sharing, no links to other sites and no popup advertising.</p>
  <p class="block body" style="top:663px;left:110px;right:110px">Plus, all Bright Quest games are aligned with the Australian Mathematics Curriculum.</p>

  <svg class="band band--bottom" viewBox="0 0 560 90" preserveAspectRatio="none">
    <path d="M0 90V62C120 66 230 62 290 40C330 20 380 10 560 14V90Z" fill="var(--teal)"/>
    <path d="M0 62C120 66 230 62 290 40C330 20 380 10 560 14V8C380 4 326 14 284 36C226 58 120 60 0 56Z" fill="var(--red)"/>
  </svg>
</section>

<section class="page page--back">
  <div class="photo-wash" style="height:360px" role="img" aria-label="Faded photo of cheering students in a classroom"></div>
  <svg class="band band--top" viewBox="0 0 560 120" preserveAspectRatio="none">
    <path d="M0 0H560V30C470 22 400 40 360 80C330 110 240 112 0 82Z" fill="var(--teal)"/>
    <path d="M0 82C240 112 330 110 360 80C400 40 470 22 560 30V38C470 30 410 50 370 86C335 118 240 120 0 90Z" fill="var(--red)"/>
  </svg>
  <div class="brand"><span class="brand__dot"></span>Bright Quest Appeal</div>

  <p class="block kicker" style="top:128px;font-size:17px">All set up online for you!</p>
  <p class="block tagline" style="top:151px;font-size:11.5px">Builds confidence in maths for students!</p>
  <h1 class="block headline headline--lg" style="top:168px">Easy to run!</h1>
  <p class="block games-title" style="top:233px">Here is how it works:</p>

  <ul class="steps">
    <li>Let us know how many memberships you need for your Bright Quest Appeal</li>
    <li>We will send you our website access code for those memberships.</li>
    <li>Download our fundraising letter, photocopy and give to parents to collect funds. (See our website for more details.)</li>
    <li>On the website, each year level has a set of maths challenges for students to solve.</li>
    <li>Once completed students may download a certificate of congratulations.</li>
  </ul>

  <p class="block games-title" style="top:456px;left:20px;right:20px">Over 260 maths games for Foundation to Grade 6!</p>
  <div class="games" style="top:478px">
    <div class="game game--1" role="img" aria-label="Game 1 screenshot, preschool"></div>
    <div class="game game--2" role="img" aria-label="Game 2 screenshot, foundation"></div>
    <div class="game game--3" role="img" aria-label="Game 3 screenshot, grade 1"></div>
    <div class="game game--4" role="img" aria-label="Game 4 screenshot, grade 2"></div>
  </div>
  <div class="games" style="top:552px">
    <div class="game game--5" role="img" aria-label="Game 5 screenshot, grade 3"></div>
    <div class="game game--6" role="img" aria-label="Game 6 screenshot, grade 4"></div>
    <div class="game game--7" role="img" aria-label="Game 7 screenshot, grade 5 to 6"></div>
  </div>

  <div class="contact" style="top:626px">
    <div>Promoted by:</div>
    <div class="brand-inline"><span class="brand__dot" style="width:18px;height:18px"></span>Bright Quest Appeal</div>
    <div>Visit: <a>www.fundraisingforclasses.example</a></div>
    <div>Start a maths challenge for your school:</div>
    <div>Visit: <a>www.thebrightquest.example</a></div>
    <div class="phone">or call 1300 555 018</div>
  </div>

  <svg class="band band--bottom" viewBox="0 0 560 90" preserveAspectRatio="none">
    <path d="M270 90C290 64 330 56 560 58V90Z" fill="var(--teal)"/>
    <path d="M270 90C290 64 330 56 560 58V52C330 50 286 58 262 90Z" fill="var(--red)"/>
  </svg>
</section>

</body>
</html>
```